Posters to advertise a jewellery design school

I would like two pieces of artwork designing for our jewellery design school in Kuala Lumpur Malaysia.
60cm by 180cm poster
100cm by 100cm poster

My personal style is ‘perfectly imperfect’ but we wold like to show that we give quality classes in a fun and artistic / creative environment

The posters must contain our logo and you can choose to use as many or as few images as you like to tell the story or even include hand drawn line images.

https://files.brambleshare.net/folders/7kQzWmR2pLxT8nYv__HbS3dFj6cNa9Ec?usp=sharing

Please include the following wording on the poster
So you want to be a jewellery designer?

Part time and full-time classes available in:
Silversmithing
Jewellery design and rendering
Stone setting
Gemmology
Enamelling
Computer aided design
60cm by 180cm poster
100cm by 100cm poster

The posters must contain our logo and you can choose to use as many or as few images as you like to tell the story.

Silversmithing
Stone setting
Gemmology
Enamelling
Computer aided design

60cm by 180cm poster
100cm by 100cm poster

Silversmithing
Stone setting
Gemmology
Enamelling
Computer aided design

```html
<!DOCTYPE html>
<html lang="en">
<head>
<meta charset="utf-8">
<title>Mira Kestrel Jewellery – Jewellery Design Classes</title>
<link rel="stylesheet" href="https://fonts.googleapis.com/css2?family=Cinzel:wght@400&family=Questrial&family=Tenor+Sans&display=swap">
<style>
  :root {
    --ink-white: #ffffff;
    --logo-grey: #c9c9cc;
    --night-maroon: #3a0d1c;
    --night-plum: #2a1236;
    --night-indigo: #1c1f4e;
    --night-navy: #0f2457;
    --gem-blue: #4f93cf;
    --gem-deep: #1e4f8c;
    --ring-silver: #c8d2de;
    --ring-shadow: #5d6f8c;
    --tile-white: #f3f2ef;
    --tone-gold: #c9a55a;
    --tone-opal: #3d7fa8;
    --tone-green: #6f8a4a;
    --tone-ruby: #9a3a55;
    --tone-rose: #d59a78;
  }
  html, body {
    margin: 0;
    padding: 0;
    width: 1200px;
    height: 1200px;
    overflow: hidden;
    background: var(--night-navy);
  }
  .poster {
    position: relative;
    width: 1200px;
    height: 1200px;
    overflow: hidden;
    color: var(--ink-white);
  }
  .backdrop {
    position: absolute;
    inset: 0;
    background:
      radial-gradient(ellipse 90px 70px at 440px 330px, rgba(170,170,200,0.35) 0, rgba(0,0,0,0) 100%),
      radial-gradient(ellipse 90px 80px at 790px 300px, rgba(170,180,200,0.35) 0, rgba(0,0,0,0) 100%),
      radial-gradient(ellipse 80px 60px at 1010px 650px, rgba(90,150,190,0.45) 0, rgba(0,0,0,0) 100%),
      radial-gradient(ellipse 60px 60px at 1100px 290px, rgba(110,90,170,0.4) 0, rgba(0,0,0,0) 100%),
      radial-gradient(ellipse 220px 160px at 180px 760px, rgba(80,110,170,0.35) 0, rgba(0,0,0,0) 100%),
      radial-gradient(ellipse 300px 260px at 1000px 450px, rgba(120,70,150,0.35) 0, rgba(0,0,0,0) 100%),
      linear-gradient(180deg, var(--night-maroon) 0%, var(--night-plum) 30%, var(--night-indigo) 62%, var(--night-navy) 100%);
  }
  .feature-ring {
    position: absolute;
    left: 398px;
    top: 448px;
    width: 340px;
    height: 340px;
    border-radius: 50%;
    background: radial-gradient(circle at 50% 50%,
      var(--gem-blue) 0, var(--gem-deep) 52px, #dfe6ee 60px, var(--ring-silver) 72px,
      #8fa0b8 100px, var(--ring-silver) 130px, #7d8fa9 150px, var(--ring-shadow) 165px, rgba(40,50,90,0) 172px);
    box-shadow: 0 0 60px rgba(120,160,210,0.25);
  }
  .brand {
    position: absolute;
    top: 0;
    left: 0;
    width: 1200px;
    text-align: center;
    font-family: "Questrial", sans-serif;
    color: var(--logo-grey);
  }
  .brand-name {
    position: absolute;
    top: 182px;
    width: 100%;
    font-size: 44px;
    letter-spacing: 1px;
    line-height: 1;
  }
  .brand-sub {
    position: absolute;
    top: 235px;
    width: 100%;
    font-size: 25px;
    letter-spacing: 3px;
    line-height: 1;
  }
  .headline {
    position: absolute;
    top: 312px;
    left: 0;
    width: 1200px;
    text-align: center;
    font-family: "Cinzel", serif;
    margin: 0;
    font-weight: 400;
  }
  .headline-lead {
    display: block;
    font-size: 52px;
    line-height: 62px;
  }
  .headline-main {
    display: block;
    margin-top: 12px;
    font-size: 72px;
    line-height: 86px;
    letter-spacing: -1px;
  }
  .offer {
    position: absolute;
    left: 48px;
    top: 700px;
    margin: 0;
    font-family: "Tenor Sans", sans-serif;
    font-variant: small-caps;
    font-weight: 400;
    font-size: 51px;
    letter-spacing: 1px;
    line-height: 1;
    white-space: nowrap;
  }
  .courses {
    position: absolute;
    left: 50px;
    top: 800px;
    margin: 0;
    padding: 0;
    list-style: none;
    font-family: "Tenor Sans", sans-serif;
    font-variant: small-caps;
    font-size: 50px;
    letter-spacing: 1.5px;
    line-height: 58.2px;
    white-space: nowrap;
  }
  .showcase-tile {
    position: absolute;
    background-color: var(--tile-white);
  }
  .tile-pendants {
    left: 851px; top: 838px; width: 145px; height: 148px;
    background-image:
      radial-gradient(ellipse 30px 24px at 72px 44px, var(--tone-opal) 0, rgba(61,127,168,0) 100%),
      radial-gradient(ellipse 34px 30px at 92px 106px, rgba(60,60,60,0.55) 0, rgba(0,0,0,0) 100%),
      radial-gradient(ellipse 20px 16px at 40px 104px, var(--tone-gold) 0, rgba(201,165,90,0) 100%);
  }
  .tile-stacking {
    left: 1003px; top: 838px; width: 147px; height: 148px;
    background-image:
      radial-gradient(ellipse 62px 26px at 74px 66px, rgba(201,165,90,0.9) 0, rgba(111,138,74,0.5) 60%, rgba(0,0,0,0) 100%),
      linear-gradient(180deg, rgba(0,0,0,0) 40%, rgba(180,185,195,0.7) 55%, rgba(200,205,212,0.5) 80%, rgba(0,0,0,0) 95%);
  }
  .tile-cluster {
    left: 632px; top: 996px; width: 212px; height: 142px;
    background-image:
      radial-gradient(ellipse 38px 40px at 104px 70px, rgba(40,40,40,0.55) 0, var(--tone-green) 45%, rgba(111,138,74,0.4) 75%, rgba(0,0,0,0) 100%),
      radial-gradient(ellipse 20px 14px at 104px 112px, var(--tone-gold) 0, rgba(201,165,90,0) 100%);
  }
  .tile-gemring {
    left: 851px; top: 996px; width: 145px; height: 142px;
    background-image:
      radial-gradient(ellipse 22px 22px at 76px 62px, var(--tone-ruby) 0, rgba(154,58,85,0.7) 60%, rgba(0,0,0,0) 100%),
      radial-gradient(ellipse 48px 34px at 72px 64px, rgba(120,125,135,0.6) 0, rgba(0,0,0,0) 100%);
  }
  .tile-chains {
    left: 1003px; top: 996px; width: 147px; height: 142px;
    background-image:
      radial-gradient(ellipse 40px 60px at 36px 76px, rgba(213,154,120,0.75) 0, rgba(0,0,0,0) 100%),
      radial-gradient(ellipse 50px 56px at 100px 62px, rgba(175,180,188,0.75) 0, rgba(0,0,0,0) 100%);
  }
</style>
</head>
<body>
  <main class="poster">
    <div class="backdrop" role="img" aria-label="Dark photograph of purple and blue crystals"></div>
    <div class="feature-ring" role="img" aria-label="Close-up photograph of a textured silver ring set with a blue cabochon stone"></div>

    <header class="brand">
      <div class="brand-name">MIRA KESTREL</div>
      <div class="brand-sub">jewellery</div>
    </header>

    <h1 class="headline">
      <span class="headline-lead">You Want To Be A</span>
      <span class="headline-main">JEWELLERY DESIGNER?</span>
    </h1>

    <h2 class="offer">Part time and Full-time Classes Available in:</h2>

    <ul class="courses">
      <li>Silversmithing</li>
      <li>Jewellery design and rendering</li>
      <li>Stone setting</li>
      <li>Gemmology</li>
      <li>Enamelling</li>
      <li>Computer aided design</li>
    </ul>

    <div class="showcase-tile tile-pendants" role="img" aria-label="Photograph of opal and gold drop pendant earrings on white"></div>
    <div class="showcase-tile tile-stacking" role="img" aria-label="Photograph of silver stacking rings set with gold bezels and gemstones"></div>
    <div class="showcase-tile tile-cluster" role="img" aria-label="Photograph of an ornate cluster ring with green stones and gold"></div>
    <div class="showcase-tile tile-gemring" role="img" aria-label="Photograph of a silver ring with a pink cushion-cut gemstone"></div>
    <div class="showcase-tile tile-chains" role="img" aria-label="Photograph of rose gold and silver handmade chains and a cuff"></div>
  </main>
</body>
</html>
```